Club sale for moms — 3 static banners

Toddla is the largest daily deal site for moms, kids and babies in Russia, which provides offers with discounts up to 70%.
We need 3 banners for our flash sale, all banners must be on a white background, all must be static and be in 2 versions, so when you hover over banner the picture changes. Banners' style should differ from other banners which refer to deals (like bimbly's banners "Invite a friend, earn $20", they are attached).
Purpose: filling the empty space on the main page in case of absence of the necessary number of deals' banners. The example of our main page is attached.
1st static banner:
474px × 308px
text: Пригласите друга — получите бонус на следующую покупку!
That text means: Invite a friend and get a bonus for shopping.
After clicking on that banner a client will go to the site section "Invites".
The text means: Invite a friend and get a bonus for shopping.
2nd static banner:
308px × 199px
Text: Доставка по всей России. Оплата при получении.
After clicking on that banner a client will go to the site section about delivery.
The text means: Delivery all over Russia, pay on getting.
3rd static banner:
308px × 199px
Text:
Гарантия лучшей цены!
The text means:
Best price guarantee
Target Market(s)
moms
Industry/Entity Type
Club
Look and feel
Each slider illustrates characteristics of the customer's brand and the style your logo design should communicate.

```html
<!DOCTYPE html>
<html lang="en">
<head>
<meta charset="utf-8">
<title>Toddla — Invite a friend banner</title>
<link rel="stylesheet" href="https://fonts.googleapis.com/css2?family=Anton&family=Arimo:wght@400;700&display=swap">
<style>
  :root {
    --white: #ffffff;
    --pink: #e3137c;
    --pink-deep: #c4086a;
    --pink-light: #f24a9e;
    --logo-pink: #c81f86;
    --blanket: #e9e8e7;
    --blanket-shade: #cfcdcc;
    --skin: #f1cdb6;
    --skin-warm: #e8b597;
  }
  html, body {
    margin: 0;
    padding: 0;
    overflow: hidden;
    background: var(--white);
  }
  .banner {
    position: relative;
    width: 988px;
    height: 1200px;
    overflow: hidden;
    background: var(--white);
  }
  .hero-photo {
    position: absolute;
    left: 0;
    top: 0;
    width: 988px;
    height: 660px;
    background:
      radial-gradient(ellipse 330px 250px at 430px 280px, var(--skin) 0%, var(--skin) 55%, rgba(241,205,182,0) 100%),
      radial-gradient(ellipse 190px 200px at 720px 230px, var(--skin-warm) 0%, rgba(232,181,151,0.6) 50%, rgba(232,181,151,0) 100%),
      radial-gradient(ellipse 260px 120px at 90px 320px, var(--blanket-shade) 0%, rgba(207,205,204,0) 100%),
      linear-gradient(180deg, var(--blanket) 0%, #f3f2f1 30%, #dedcdb 62%, #f2f2f2 82%, var(--white) 100%);
  }
  .bonus-badge {
    position: absolute;
    left: 329px;
    top: 538px;
    width: 330px;
    height: 330px;
  }
  .bonus-amount {
    position: absolute;
    left: 329px;
    top: 584px;
    width: 330px;
    text-align: center;
    font-family: "Anton", "Impact", sans-serif;
    color: var(--white);
    line-height: 1;
  }
  .bonus-amount .value {
    display: block;
    font-size: 114px;
    letter-spacing: 2px;
  }
  .bonus-amount .currency {
    display: block;
    margin-top: 8px;
    font-size: 60px;
    letter-spacing: 3px;
  }
  .invite-strip {
    position: absolute;
    left: 0;
    top: 880px;
    width: 940px;
    height: 96px;
    background: linear-gradient(90deg, var(--pink-deep) 0%, var(--pink) 45%, var(--pink-light) 100%);
    clip-path: polygon(0 0, 96% 0, 100% 50%, 96% 100%, 0 100%);
    display: flex;
    align-items: center;
  }
  .invite-strip p {
    margin: 0 0 0 54px;
    font-family: "Arimo", "Arial", sans-serif;
    font-size: 43px;
    color: var(--white);
    white-space: nowrap;
  }
  .brand {
    position: absolute;
    left: 0;
    top: 1036px;
    width: 988px;
    display: flex;
    justify-content: center;
    align-items: center;
    gap: 16px;
  }
  .brand-dot {
    width: 30px;
    height: 30px;
    border-radius: 50%;
    background: var(--logo-pink);
  }
  .brand-name {
    font-family: "Arimo", "Arial", sans-serif;
    font-weight: 700;
    font-size: 118px;
    color: var(--logo-pink);
    line-height: 1;
  }
</style>
</head>
<body>
  <div class="banner">
    <div class="hero-photo" role="img" aria-label="Photo of a smiling baby peeking out from under a white blanket on a white bed"></div>

    <svg class="bonus-badge" viewBox="0 0 300 300" aria-hidden="true">
      <defs>
        <radialGradient id="badgeFill" cx="45%" cy="35%" r="70%">
          <stop offset="0%" stop-color="#f870b6"/>
          <stop offset="60%" stop-color="#e3137c"/>
          <stop offset="100%" stop-color="#b80762"/>
        </radialGradient>
      </defs>
      <g fill="#e3137c" transform="translate(150 150)">
        <rect x="-104" y="-104" width="208" height="208"/>
        <rect x="-104" y="-104" width="208" height="208" transform="rotate(15)"/>
        <rect x="-104" y="-104" width="208" height="208" transform="rotate(30)"/>
        <rect x="-104" y="-104" width="208" height="208" transform="rotate(45)"/>
        <rect x="-104" y="-104" width="208" height="208" transform="rotate(60)"/>
        <rect x="-104" y="-104" width="208" height="208" transform="rotate(75)"/>
      </g>
      <circle cx="150" cy="150" r="124" fill="#ffffff"/>
      <circle cx="150" cy="150" r="116" fill="url(#badgeFill)"/>
    </svg>
    <div class="bonus-amount">
      <span class="value">20</span>
      <span class="currency">DOLLAR</span>
    </div>

    <div class="invite-strip">
      <p>Invite a friend and get a bonus for shopping.</p>
    </div>

    <div class="brand">
      <span class="brand-dot"></span>
      <span class="brand-name">Toddla</span>
    </div>
  </div>
</body>
</html>
```